Club sale for moms needs impressive design

Hi! We are kroshik.ru - largest daily deal site for moms, babies and kids in Russia, which provides offers with discounts up to 70%. We are going to run a line of seasonal DIY kits for kids.

This kits will be packed into the kraft boxes 220 mm(L) х 320mm (W) х 100mm (H).

To make a box look more like a gift, and something that moms will love to buy, we decided to make them bright, colorful and lovely.

We need a good designer for:

1. Fancy box (layout attached)

2. A template to make how-to instructions. We should be able to change text in it, insert images and it ought to have our logo (attached). These how-to manuals will be printed on A5 format.

Template is expected to have brand style and it must have:

name
text
photos
logo (attached)

Target Market(s)

Moms and kids

Industry/Entity Type

Club

Requirements
Must have
• name

place for text

place for photos

logo (attached)

```html
<!DOCTYPE html>
<html lang="en">
<head>
<meta charset="utf-8">
<title>Kroshik gift box</title>
<link href="https://fonts.googleapis.com/css2?family=Arimo:wght@700&display=swap" rel="stylesheet">
<style>
  :root {
    --paper: #ffffff;
    --kraft: #e3c3b1;
    --ink: #000000;
    --berry: #d7006f;
    --mustard: #dbbd2a;
    --snow-light: #e9eef3;
    --snow-warm: #c9a27a;
    --coat: #e0306a;
  }
  html, body {
    margin: 0;
    width: 1200px;
    height: 896px;
    overflow: hidden;
    background: var(--paper);
  }
  .box-dieline {
    display: block;
    width: 1200px;
    height: 896px;
  }
  .panel-kraft { fill: var(--kraft); }
  .panel-ink { fill: var(--ink); }
  .panel-berry { fill: var(--berry); }
  .panel-mustard { fill: var(--mustard); }
  .brand-name {
    font-family: "Arimo", Arial, sans-serif;
    font-weight: 700;
    font-size: 15px;
  }
  .brand-name--lid { fill: var(--berry); }
  .brand-name--window { fill: var(--paper); }
  .gift-line {
    font-family: "Arimo", Arial, sans-serif;
    font-weight: 700;
    font-size: 11px;
    fill: var(--berry);
  }
</style>
</head>
<body>
<svg class="box-dieline" viewBox="0 0 1000 750" preserveAspectRatio="none" xmlns="http://www.w3.org/2000/svg">
  <defs>
    <linearGradient id="window-scene" x1="0" y1="0" x2="1" y2="1">
      <stop offset="0" stop-color="var(--snow-warm)"/>
      <stop offset="0.45" stop-color="var(--snow-light)"/>
      <stop offset="0.8" stop-color="var(--coat)"/>
      <stop offset="1" stop-color="var(--snow-light)"/>
    </linearGradient>
  </defs>

  <g class="flap-top">
    <rect class="panel-ink" x="285" y="48" width="437" height="112" rx="10"/>
    <polygon class="panel-kraft" points="365,48 642,48 505,165"/>
    <text class="brand-name brand-name--lid" x="566" y="152">Kroshik</text>
  </g>

  <g class="lid-band">
    <rect class="panel-kraft" x="137" y="163" width="222" height="164" rx="8"/>
    <rect class="panel-kraft" x="130" y="210" width="20" height="62" rx="4"/>
    <rect class="panel-kraft" x="650" y="163" width="222" height="164" rx="8"/>
    <rect class="panel-kraft" x="860" y="210" width="20" height="62" rx="4"/>
    <polygon class="panel-berry" points="255,163 357,163 357,268"/>
    <polygon class="panel-berry" points="650,163 752,163 650,268"/>
    <rect class="panel-ink" x="357" y="163" width="293" height="109"/>
    <rect class="panel-kraft" x="357" y="272" width="293" height="60"/>
  </g>

  <g class="lid-front">
    <rect class="panel-kraft" x="285" y="330" width="437" height="107" rx="6"/>
  </g>

  <g class="character-face" role="img" aria-label="Mouse character face with eyes, whiskers, nose and paws on the box lid">
    <polygon class="panel-mustard" points="365,272 642,272 512,420"/>
  </g>

  <g class="window-section">
    <path class="panel-berry" d="M248,462 Q300,440 362,440 L362,605 Q300,605 248,585 Z"/>
    <path class="panel-berry" d="M646,440 Q710,440 760,462 L760,585 Q710,605 646,605 Z"/>
    <rect x="360" y="437" width="288" height="175" fill="url(#window-scene)" role="img" aria-label="Photo of a smiling girl in a pink winter coat and knitted hat in a snowy park"/>
    <text class="gift-line" x="372" y="546">A GIFT</text>
    <text class="gift-line" x="372" y="559">FOR</text>
    <text class="gift-line" x="372" y="572">MY SWEET</text>
    <text class="gift-line" x="372" y="585">GIRL</text>
    <text class="brand-name brand-name--window" x="568" y="591">Kroshik</text>
  </g>

  <g class="flap-bottom">
    <path class="panel-ink" d="M258,605 L750,605 Q760,605 760,615 L760,640 Q760,710 690,710 L318,710 Q248,710 248,640 L248,615 Q248,605 258,605 Z"/>
    <polygon class="panel-kraft" points="355,605 652,605 505,712"/>
  </g>
</svg>
</body>
</html>
```